Business Card for Coach - ready to print

Design Business Card ready to order prints www.lukasbrenner.coach

* An Overview / Background of the Business & Services
· Coaching
· Personal growth
* The Target Market / Audience you are trying to reach
· private person in different roles (self, familiy, business role)s
* Design Specifics; any preferences or ideas for Style, Colour, Imagery, etc
· See www.lukasbrenner.coach
· "simple" design
· (small) element of surprise / unusual element

* Information that will be placed in the Business Card
· Beratung und Coaching
· Address: Lukas Brenner, Talmatt 42, CH-8531 Winterthur, Mobile +41 76 254 63 07
* Do you have an existing website or Facebook page where designers can learn more about your company?
· lukasbrenner.coach

Target Market(s)

private person in different roles (self, familiy, business role)

Industry/Entity Type

Life Coaching

Contact Information for Business Card

Lukas Brenner
Talmatt 42
CH-8531 Winterthur

Mobile: +41 76 254 63 07
Email: lubr@sonnwelt.ch
www.lukasbrenner.coach

Font styles to use
Sans Serif

Colors

Designer to choose colors to be used in the design.

Requirements
Must have
• "simple" design
• element of surprise / unusual element
• Beratung & Coaching
• see www.lukasbrenner.coach for colors and so...
Nice to have
• TA Symbol (three rings on top of each other) - unsual presentation
• QR Code of Website (see if it fits in and still looks good).

```html
<!DOCTYPE html>
<html lang="de">
<head>
<meta charset="utf-8">
<title>Lukas Brenner – Visitenkarte</title>
<link rel="stylesheet" href="https://fonts.googleapis.com/css2?family=Didact+Gothic&family=Jost:wght@600&display=swap">
<style>
  :root {
    --page-bg: #d2d2d2;
    --card-bg: #b7dff6;
    --ink: #1d1d1b;
    --ink-soft: #4b5056;
    --card-shadow: rgba(0, 0, 0, 0.28);
  }
  * { box-sizing: border-box; margin: 0; padding: 0; }
  html, body {
    width: 1125px;
    height: 1200px;
    overflow: hidden;
    background: var(--page-bg);
  }
  .canvas {
    position: relative;
    width: 1125px;
    height: 1200px;
  }
  .card {
    position: absolute;
    left: 82px;
    width: 960px;
    height: 546px;
    background: var(--card-bg);
    box-shadow: 4px 6px 14px var(--card-shadow);
    color: var(--ink);
  }
  .card--front { top: 36px; }
  .card--back  { top: 618px; }

  .holder-name {
    position: absolute;
    left: 44px;
    top: 198px;
    font-family: "Jost", "Century Gothic", sans-serif;
    font-weight: 600;
    font-size: 31px;
    letter-spacing: 0.2px;
  }
  .name-rule {
    position: absolute;
    left: 44px;
    top: 266px;
    width: 586px;
    height: 4px;
    background: var(--ink);
  }
  .portrait {
    position: absolute;
    left: 626px;
    top: 164px;
    width: 218px;
    height: 218px;
  }
  .contact {
    position: absolute;
    left: 44px;
    top: 296px;
    font-family: "Didact Gothic", "Century Gothic", sans-serif;
    font-size: 23px;
    color: var(--ink-soft);
    line-height: 28px;
  }
  .contact__address { margin-bottom: 7px; }
  .contact__row {
    display: flex;
    align-items: center;
    height: 35.5px;
  }
  .contact__icon {
    width: 16px;
    height: 16px;
    margin-right: 9px;
    flex: none;
  }
  .tagline {
    position: absolute;
    left: 0;
    right: 0;
    top: 50%;
    transform: translateY(-50%);
    text-align: center;
    font-family: "Jost", "Century Gothic", sans-serif;
    font-weight: 600;
    font-size: 54px;
    letter-spacing: 0.5px;
  }
</style>
</head>
<body>
<div class="canvas">
  <section class="card card--front">
    <h1 class="holder-name">Lukas Brenner</h1>
    <div class="name-rule"></div>

    <svg class="portrait" viewBox="0 0 218 218" role="img" aria-label="Round portrait photo of Lukas Brenner">
      <defs>
        <linearGradient id="portraitTone" x1="0" y1="0" x2="0" y2="1">
          <stop offset="0" stop-color="#9a9ea3"/>
          <stop offset="0.55" stop-color="#8b8f95"/>
          <stop offset="1" stop-color="#6d7380"/>
        </linearGradient>
      </defs>
      <circle cx="109" cy="109" r="106.5" fill="url(#portraitTone)" stroke="#1d1d1b" stroke-width="3.5"/>
    </svg>

    <div class="contact">
      <p class="contact__address">Talmatt 42<br>CH-8531 Winterthur</p>
      <p class="contact__row">
        <svg class="contact__icon" viewBox="0 0 16 16" aria-hidden="true">
          <path d="M3.2 1.5 5.6 4 4.4 5.6c.9 2 2.4 3.6 4.2 4.6l1.5-1.3 2.6 2.4-1.6 2.4C6.6 13.6 2.2 9.2 1 4.1Z" fill="#1d1d1b"/>
          <path d="M9 2.2a5 5 0 0 1 4.6 4.6M9 4.6a2.6 2.6 0 0 1 2.3 2.3" fill="none" stroke="#1d1d1b" stroke-width="1.4"/>
        </svg>+41 76 254 63 07
      </p>
      <p class="contact__row">
        <svg class="contact__icon" viewBox="0 0 16 16" aria-hidden="true">
          <rect x="1" y="3" width="14" height="11" fill="#1d1d1b"/>
          <path d="M3 5.5 8 9.5l5-4" fill="none" stroke="#b7dff6" stroke-width="1.5"/>
        </svg>lubr@sonnwelt.ch
      </p>
      <p class="contact__row">
        <svg class="contact__icon" viewBox="0 0 16 16" aria-hidden="true">
          <circle cx="8" cy="8" r="7" fill="#1d1d1b"/>
          <path d="M4 4.5c1.5 0 2.5 1 2 2.5s-2 1.5-1.5 3.5M10 2.5c-.5 1.5.5 2.5 2 2.5M10.5 9c1 .5 1.5 2 1 3.5" fill="none" stroke="#b7dff6" stroke-width="1.3"/>
        </svg>www.lukasbrenner.coach
      </p>
    </div>
  </section>

  <section class="card card--back">
    <p class="tagline">Beratung &amp; Coaching</p>
  </section>
</div>
</body>
</html>
```